Brightmoor Capital Partners- Business Card

We need a professional business card that conveys confidence and trust. Strength. A modern and still yet, traditional financial planner/advisor format. I will upload a logo file or two, you do not have to use it, if it does not work for the design.

Target Market(s)

high net worth

Industry/Entity Type

Finance

Contact Information for Business Card

Address: 24853 Harlow Ave. Suite 610, Huntington Beach, CA 90318, website: brightmoorcapital.example, ph # (555) 276-1948, email address: mpellegrin@brightmoorcapital.example

```html
<!DOCTYPE html>
<html lang="en">
<head>
<meta charset="utf-8">
<title>Brightmoor Capital Partners – Business Card</title>
<link href="https://fonts.googleapis.com/css2?family=Montserrat:wght@500;700&family=Playfair+Display+SC:wght@400&display=swap" rel="stylesheet">
<style>
  :root {
    --bg: #3a3a3c;
    --paper: #ffffff;
    --ink: #1a1a1a;
    --black-card: #141414;
    --gold: #b98a26;
    --gold-light: #e2c46a;
    --gold-deep: #9a6f16;
    --gold-gradient: linear-gradient(90deg, var(--gold-deep) 0%, var(--gold) 35%, var(--gold-light) 65%, var(--gold) 100%);
  }
  * { box-sizing: border-box; margin: 0; padding: 0; }
  html, body { width: 1200px; height: 1200px; overflow: hidden; }
  body {
    background: var(--bg);
    display: flex;
    flex-direction: column;
    align-items: center;
    justify-content: space-evenly;
    font-family: "Montserrat", Arial, sans-serif;
  }
  .card {
    position: relative;
    width: 860px;
    height: 491px;
    border-radius: 42px;
    overflow: hidden;
  }

  /* Front */
  .card-front { background: var(--paper); color: var(--ink); }
  .brand-block {
    position: absolute;
    left: 500px;
    top: 120px;
    width: 300px;
    display: flex;
    flex-direction: column;
    align-items: center;
    gap: 22px;
    text-align: center;
  }
  .brand-square {
    width: 110px;
    height: 110px;
    border: 4px solid var(--gold);
    border-radius: 14px;
  }
  .brand-name {
    font-family: "Montserrat", Arial, sans-serif;
    font-weight: 500;
    font-size: 26px;
    line-height: 1.25;
    color: var(--gold);
  }
  .identity {
    position: absolute;
    left: 86px;
    top: 222px;
  }
  .full-name {
    font-weight: 700;
    font-size: 44px;
    letter-spacing: 0.5px;
    color: var(--gold);
    line-height: 1;
  }
  .position {
    font-weight: 500;
    font-size: 24px;
    letter-spacing: 1px;
    margin-top: 4px;
    margin-left: 12px;
  }
  .contact-list {
    list-style: none;
    margin-top: 14px;
    margin-left: 40px;
    font-weight: 500;
    font-size: 22px;
    line-height: 29px;
  }
  .contact-list li { display: flex; align-items: flex-start; gap: 12px; }
  .contact-list .icon { flex: 0 0 24px; height: 29px; display: flex; align-items: center; }
  .contact-list .icon svg { width: 22px; height: 22px; fill: var(--gold); }
  .band-gold {
    position: absolute;
    left: 0; bottom: 0;
    width: 570px; height: 30px;
    background: var(--gold-gradient);
  }
  .band-black {
    position: absolute;
    left: 584px; bottom: 0;
    right: 0; height: 30px;
    background: var(--black-card);
  }

  /* Back */
  .card-back {
    background: radial-gradient(ellipse at 60% 35%, #222 0%, var(--black-card) 70%);
    border: 3px solid var(--gold);
    display: flex;
    align-items: center;
    justify-content: center;
    gap: 22px;
  }
  .back-square {
    width: 64px;
    height: 64px;
    border: 3px solid var(--gold);
    border-radius: 8px;
  }
  .back-name {
    font-family: "Playfair Display SC", Georgia, serif;
    font-weight: 400;
    font-size: 42px;
    letter-spacing: 1px;
    color: var(--gold);
  }
</style>
</head>
<body>

  <section class="card card-front">
    <div class="brand-block">
      <div class="brand-square"></div>
      <div class="brand-name">Brightmoor Capital Partners</div>
    </div>

    <div class="identity">
      <h1 class="full-name">FULL NAME</h1>
      <p class="position">POSITION</p>
      <ul class="contact-list">
        <li><span class="icon"><svg viewBox="0 0 24 24"><path d="M6.6 10.8a15.1 15.1 0 0 0 6.6 6.6l2.2-2.2c.3-.3.7-.4 1-.2 1.1.4 2.3.6 3.6.6.6 0 1 .4 1 1V20c0 .6-.4 1-1 1A17 17 0 0 1 3 4c0-.6.4-1 1-1h3.5c.6 0 1 .4 1 1 0 1.3.2 2.5.6 3.6.1.3 0 .7-.2 1z"/></svg></span>(000) 000 0000</li>
        <li><span class="icon"><svg viewBox="0 0 24 24"><path d="M2 5h20v14H2z M4 7v.3l8 5.2 8-5.2V7z" fill-rule="evenodd"/></svg></span>email@company.com</li>
        <li><span class="icon"><svg viewBox="0 0 24 24"><path d="M12 2a10 10 0 1 0 0 20 10 10 0 0 0 0-20zm6.9 6h-3a15 15 0 0 0-1.3-3.9A8 8 0 0 1 18.9 8zM12 4c.8 1.1 1.5 2.5 1.9 4h-3.8c.4-1.5 1.1-2.9 1.9-4zM4.3 14a8 8 0 0 1 0-4h3.4a16 16 0 0 0 0 4zm.8 2h3a15 15 0 0 0 1.3 3.9A8 8 0 0 1 5.1 16zm3-8h-3a8 8 0 0 1 4.3-3.9A15 15 0 0 0 8.1 8zM12 20c-.8-1.1-1.5-2.5-1.9-4h3.8c-.4 1.5-1.1 2.9-1.9 4zm2.3-6H9.7a14 14 0 0 1 0-4h4.6a14 14 0 0 1 0 4zm.3 5.9a15 15 0 0 0 1.3-3.9h3a8 8 0 0 1-4.3 3.9zm1.7-5.9a16 16 0 0 0 0-4h3.4a8 8 0 0 1 0 4z"/></svg></span>www.company.com</li>
        <li><span class="icon"><svg viewBox="0 0 24 24"><path d="M12 2a7 7 0 0 0-7 7c0 5.2 7 13 7 13s7-7.8 7-13a7 7 0 0 0-7-7zm0 9.5A2.5 2.5 0 1 1 12 6.5a2.5 2.5 0 0 1 0 5z"/></svg></span>123 Name Street, 000<br>Your City, 00000-000</li>
      </ul>
    </div>

    <div class="band-gold"></div>
    <div class="band-black"></div>
  </section>

  <section class="card card-back">
    <div class="back-square"></div>
    <div class="back-name">Brightmoor Capital Partners</div>
  </section>

</body>
</html>
```